Website for Boutique Property Consultancy in UK

We are looking to designing a website for our Property Consultancy Services that follows a minimalistic clean style that is also bold and intriguing.
The website will be based on one landing page and a link to Linkora Page and email link.

Dominant features will be the company logo or icon and colours.

Brand colours provided for guidance.

Looking to achieve a minimalistic clean style that is also bold and intriguing.

"Updated"
Page 1 - Landing Page with the Hyperlinks to Pick a Service, Training Portal and Amber Quill Portal. example landing page https://plumweave.co.uk/

Page 2 - Shows all the Services and Sectors

Target Market(s)

Occupier Clients, Tech Companies, Property Developers, Infrastructure Clients and Major Consultants

Industry/Entity Type

Construction

Coding

Coded - Design and coding required

Number of Pages Required

2 page

Font styles to use
Other font styles liked:
• Century Gothic or Futuris (Headings)

Colors
0054AA
0677BA
7BADD7
CADEEF
E8F1F8
00AB8E
00BBA5
67D7C9
C6EFE9
E9F9F6

Requirements
Must have
• Company Logo, link to enquiry and Linkora

```html
<!DOCTYPE html>
<html lang="en">
<head>
<meta charset="utf-8">
<title>Larch Vale — Property Consultancy</title>
<link rel="stylesheet" href="https://fonts.googleapis.com/css2?family=Lexend:wght@300;400;500;600&display=swap">
<style>
  :root {
    --panel: #2c3150;
    --panel-footer: #272b47;
    --ink: #ffffff;
    --ink-soft: #e4e6ef;
    --accent: #22b573;
    --rule: #c9cbd6;
    --visual-top: #2a3447;
    --visual-bottom: #141d2c;
  }
  * { box-sizing: border-box; margin: 0; padding: 0; }
  html, body { width: 1200px; height: 750px; overflow: hidden; background: #e3e3e3; }
  body { font-family: "Lexend", sans-serif; color: var(--ink); }
  .landing { position: relative; width: 1200px; height: 750px; display: flex; }
  .intro {
    position: relative; width: 578px; height: 750px; background: var(--panel);
  }
  .brand {
    position: absolute; left: 92px; top: 80px;
    display: flex; align-items: center; gap: 14px;
    font-size: 50px; font-weight: 400; letter-spacing: 1px; color: var(--ink);
  }
  .brand-mark { width: 14px; height: 14px; border-radius: 50%; background: var(--accent); }
  .headline {
    position: absolute; left: 94px; top: 210px;
    font-size: 39px; line-height: 44px; font-weight: 300; letter-spacing: 1.4px;
  }
  .headline strong { font-weight: 600; }
  .portal-links { position: absolute; left: 105px; top: 384px; width: 346px; list-style: none; }
  .portal-link {
    display: flex; justify-content: space-between; align-items: center;
    height: 62px; padding-right: 6px;
    font-size: 19px; font-weight: 300; color: var(--ink-soft); text-decoration: none;
    border-bottom: 1.5px solid var(--rule);
  }
  .portal-links li:last-child .portal-link { border-bottom: none; }
  .portal-link.is-active { color: var(--accent); }
  .portal-link svg { width: 16px; height: 16px; flex: none; }
  .site-footer {
    position: absolute; left: 0; bottom: 0; width: 578px; height: 72px;
    background: var(--panel-footer); display: flex; align-items: center;
    padding-left: 81px;
  }
  .copyright { font-size: 12.5px; font-weight: 300; color: var(--ink-soft); width: 288px; white-space: nowrap; }
  .footer-links { display: flex; align-items: center; gap: 20px; }
  .footer-links a { color: var(--ink); text-decoration: none; font-size: 13px; font-weight: 500; display: flex; align-items: center; }
  .footer-links svg { width: 22px; height: 18px; }
  .member-badge { width: 60px; height: 22px; border-radius: 11px; background: var(--ink-soft); opacity: .85; margin-left: 4px; }
  .hero-visual {
    position: relative; flex: 1; height: 750px;
    background: linear-gradient(180deg, var(--visual-top) 0%, var(--visual-bottom) 100%);
  }
  .enquiry-button {
    position: absolute; left: 410px; top: 42px; width: 144px; height: 42px;
    display: flex; align-items: center; justify-content: center;
    border: 1.5px solid var(--ink); color: var(--ink); text-decoration: none;
    font-size: 16px; font-weight: 500; letter-spacing: .8px;
  }
</style>
</head>
<body>
<main class="landing">
  <section class="intro">
    <div class="brand"><span>Larch Vale</span><span class="brand-mark"></span></div>
    <h1 class="headline">Delivering Value<br>and <strong>Redefining</strong><br><strong>Boundaries</strong></h1>
    <ul class="portal-links">
      <li><a class="portal-link is-active" href="#">Pick a services
        <svg viewBox="0 0 16 16" fill="none" stroke="currentColor" stroke-width="1.5"><path d="M2 8h12M9 3l5 5-5 5"/></svg></a></li>
      <li><a class="portal-link" href="#">Training Portal
        <svg viewBox="0 0 16 16" fill="none" stroke="currentColor" stroke-width="1.5"><path d="M2 8h12M9 3l5 5-5 5"/></svg></a></li>
      <li><a class="portal-link" href="#">Amber Quill Portal
        <svg viewBox="0 0 16 16" fill="none" stroke="currentColor" stroke-width="1.5"><path d="M2 8h12M9 3l5 5-5 5"/></svg></a></li>
    </ul>
    <footer class="site-footer">
      <p class="copyright">© larchvale. All Rights Reserved</p>
      <nav class="footer-links">
        <a href="#" aria-label="Email us"><svg viewBox="0 0 22 18" fill="none" stroke="currentColor" stroke-width="1.6"><rect x="1.5" y="2" width="19" height="14" rx="2"/><path d="M2 3l9 7 9-7"/></svg></a>
        <a href="#">Linkora</a>
        <span class="member-badge" aria-label="Professional body membership"></span>
      </nav>
    </footer>
  </section>
  <section class="hero-visual" role="img" aria-label="Photograph of city office towers seen from below">
    <a class="enquiry-button" href="#">Talk with us</a>
  </section>
</main>
</body>
</html>
```